jewellery store flyer

Front to show
-company name and logo
underneath of company name, I want " The perfect creation" to be written.
-background bright tone jewellery or model wearing jewellery(prefer engagement and wedder or wedder set)

--------------------------------------------------------------
Back to show list of service and brief map of location
with addresss and contact detail

introducing newly established jewellery store with exclusive and unique jewellery. We offer you
-specialized in hand made jewellery
-on site jeweller and designer
-repair and restoring
-laser engraving and laser solder

4/31 Tarrawin Crescent Marrowvale ACT 2619
02) 6148 3072
Enquiry: marlow.k@postvane.com
---------------------------------------------------------------------
I have enclosed mockups that I made by myself, to show what I was thinking. this is just for reference. New flyer doesn't need to look the same.

I don't mind either holizontal nor vertical.
I don't mind if you add text or remove text that I have written above.
I want flyer to look morden and neat.

Good luck to you & me and enjoy creation.
Kind regards,
Pearl

Target Market(s)

introducing newly established store.
aiming for engagement & wedding rings and remakes

Industry/Entity Type

It Company

Font styles to use
Other font styles liked:
• Monotype corsive for script but name and address for SERIF

Colors

Designer to choose colors to be used in the design.

Requirements
Must have
• background photo including jewellery
• company name and address
• service detail
Nice to have
• brief map of location( I have red circled few places that people know more on the map I attached here.)
• Map to be simplified please.
• Please do not use Google map directly.
• Opening hours: Mon-Fri 9.30 to 5.30 Sat 10.00 to 5

```html
<!DOCTYPE html>
<html lang="en">
<head>
<meta charset="utf-8">
<title>Linden Jewellery Flyer</title>
<link rel="stylesheet" href="https://fonts.googleapis.com/css2?family=Cinzel:wght@400;700&family=Libre+Baskerville:wght@400;700&family=Pinyon+Script&display=swap">
<style>
  :root {
    --page-bg: #2a2a2a;
    --ink-white: #f4f1ec;
    --ink-soft: #e6e1d8;
    --gold-light: #f7d36b;
    --gold: #e2a92a;
    --gold-deep: #b27812;
    --card-black: #0b0b0b;
    --map-cream: #fbf1df;
  }
  * { margin: 0; padding: 0; box-sizing: border-box; }
  html, body { width: 1200px; height: 1200px; overflow: hidden; }
  body { background: var(--page-bg); position: relative; font-family: "Libre Baskerville", Georgia, serif; color: var(--ink-white); }

  .flyer { position: absolute; top: 250px; width: 525px; height: 736px; overflow: hidden; box-shadow: 0 6px 22px rgba(0,0,0,.55); }
  .flyer--front { left: 49px; background: #1e2322; }
  .flyer--back { left: 630px; background: var(--card-black); }

  /* Front */
  .model-photo { position: absolute; inset: 0;
    background:
      radial-gradient(ellipse 46% 38% at 66% 40%, #d9b49c 0%, #b88a70 40%, rgba(60,55,50,0) 75%),
      radial-gradient(ellipse 40% 22% at 70% 10%, #7a5a3a 0%, rgba(40,35,30,0) 80%),
      radial-gradient(ellipse 50% 30% at 85% 92%, #c9a48e 0%, rgba(40,40,38,0) 80%),
      linear-gradient(90deg, #1b201f 0%, #2a302f 45%, #3a3a36 100%); }
  .brand__mark { position: absolute; left: 68px; top: 191px; width: 70px; height: 70px; border: 2px solid var(--ink-soft); border-radius: 50%; }
  .brand__name { position: absolute; left: 28px; top: 290px; font-family: "Cinzel", serif; font-weight: 400; font-size: 17px; color: var(--ink-white); white-space: nowrap; }
  .headline { position: absolute; left: 36px; top: 406px; }
  .headline__line { display: block; font-family: "Cinzel", serif; font-weight: 700; color: var(--ink-white); line-height: 1; }
  .headline__the { font-size: 50px; font-weight: 400; }
  .headline__perfect { font-size: 52px; margin-top: 12px; }
  .headline__script { display: block; font-family: "Pinyon Script", cursive; font-size: 98px; line-height: 1; margin-top: -8px; margin-left: -6px;
    background: linear-gradient(180deg, var(--gold-light), var(--gold) 55%, var(--gold-deep));
    -webkit-background-clip: text; background-clip: text; color: transparent; }

  /* Back */
  .back-photo { position: absolute; inset: 0;
    background:
      radial-gradient(ellipse 32% 26% at 78% 42%, rgba(70,55,45,.55) 0%, rgba(0,0,0,0) 80%),
      linear-gradient(180deg, #141414 0%, #0b0b0b 60%, #050505 100%); }
  .intro { position: absolute; left: 38px; top: 36px; font-size: 14px; line-height: 19px; color: var(--ink-white); white-space: nowrap; }
  .offer-title { position: absolute; left: 43px; top: 92px; font-size: 15.5px; font-weight: 700; padding: 0 2px 6px; border-bottom: 2px solid var(--ink-soft); }
  .services { position: absolute; left: 42px; top: 144px; list-style: none; }
  .services li { display: flex; align-items: center; height: 38.5px; font-size: 15px; }
  .services svg { width: 24px; height: 24px; margin-right: 11px; }
  .map { position: absolute; left: 135px; top: 338px; width: 258px; height: 169px; background: var(--map-cream); border: 9px solid #fff; outline: 1px solid #ddd; }
  .location { position: absolute; left: 150px; top: 542px; display: flex; align-items: center; }
  .location svg { width: 34px; height: 40px; margin-right: 36px; }
  .location__text { font-size: 14.5px; font-weight: 700; line-height: 17px; white-space: nowrap; }
  .contact { position: absolute; left: 40px; top: 650px; list-style: none; }
  .contact li { display: flex; align-items: center; height: 28px; font-size: 14px; font-weight: 700; }
  .contact svg { width: 14px; height: 14px; margin-right: 13px; }
  .gems-photo { position: absolute; left: 240px; top: 615px; width: 285px; height: 121px;
    background: radial-gradient(ellipse 50% 55% at 55% 45%, rgba(200,210,220,.45), rgba(90,100,110,.2) 55%, rgba(0,0,0,0) 80%); }
</style>
</head>
<body>
  <section class="flyer flyer--front">
    <div class="model-photo" role="img" aria-label="Portrait of a model with an elegant updo wearing a pearl necklace and earrings"></div>
    <div class="brand__mark"></div>
    <p class="brand__name">Linden Jewellery</p>
    <h1 class="headline">
      <span class="headline__line headline__the">THE</span>
      <span class="headline__line headline__perfect">PERFECT</span>
      <span class="headline__script">Creation</span>
    </h1>
  </section>

  <section class="flyer flyer--back">
    <div class="back-photo" role="img" aria-label="Dark damask pattern with a faint portrait of the model in the background"></div>
    <p class="intro">Introducing Newly Established Jewellery Store With Exclusive<br>And Unique Jewellery.</p>
    <h2 class="offer-title">We Offer You</h2>
    <ul class="services">
      <li><svg viewBox="0 0 24 24"><path d="M12 1 23 12 12 23 1 12Z" fill="#e9b430"/><path d="M12 1 23 12H1Z" fill="#f8d360"/></svg>Specialized In Hand Made Jewellery.</li>
      <li><svg viewBox="0 0 24 24"><path d="M12 1 23 12 12 23 1 12Z" fill="#e9b430"/><path d="M12 1 23 12H1Z" fill="#f8d360"/></svg>On Site Jeweller And Designer.</li>
      <li><svg viewBox="0 0 24 24"><path d="M12 1 23 12 12 23 1 12Z" fill="#e9b430"/><path d="M12 1 23 12H1Z" fill="#f8d360"/></svg>Repair And Restoring.</li>
      <li><svg viewBox="0 0 24 24"><path d="M12 1 23 12 12 23 1 12Z" fill="#e9b430"/><path d="M12 1 23 12H1Z" fill="#f8d360"/></svg>Laser Engraving And Laser Solder.</li>
    </ul>
    <div class="map" role="img" aria-label="Simplified street map showing the store location and nearby landmarks"></div>
    <div class="location">
      <svg viewBox="0 0 34 40"><path d="M17 3a8 8 0 0 0-8 8c0 6 8 15 8 15s8-9 8-15a8 8 0 0 0-8-8Z" fill="none" stroke="#fff" stroke-width="2.4"/><circle cx="17" cy="11" r="3" fill="#fff"/><path d="M9 24 3 37h28l-6-13" fill="none" stroke="#fff" stroke-width="2.4"/></svg>
      <p class="location__text">4/31 Tarrawin Crescent<br>Marrowvale ACT 2619</p>
    </div>
    <ul class="contact">
      <li><svg viewBox="0 0 14 14"><path d="M3 1l2.5 3-1.5 1.5c.8 1.8 2 3 3.5 3.5L9 7.5l3 2.5-1.5 2.5C6 12 2 8 1.5 3Z" fill="#fff"/></svg>(02) 6148 3072</li>
      <li><svg viewBox="0 0 14 14"><circle cx="7" cy="7" r="6" fill="none" stroke="#fff" stroke-width="1.6"/><rect x="4" y="5" width="6" height="4" fill="none" stroke="#fff" stroke-width="1.2"/></svg>marlow.k@postvane.com</li>
    </ul>
    <div class="gems-photo" role="img" aria-label="Three sparkling cut diamonds with reflections"></div>
  </section>
</body>
</html>
```